SloPitch Ad

Looking for a creative eye-catching ad to go on the front page of my website to promote a softball league. Ad dimensions needs to be 1194 by 624, or in that ratio so that it can also be used on facebook.
I have attached some graphics that I have seen on other sites that I like for general ideas. Will need the colors to match with my website (www.pkvathletics.com) but logo is not necessary

```html
<!DOCTYPE html>
<html lang="en">
<head>
<meta charset="utf-8">
<title>Spring Swing – Softball and Kickball Tournament</title>
<link href="https://fonts.googleapis.com/css2?family=Bebas+Neue&family=PT+Sans+Narrow:wght@400;700&display=swap" rel="stylesheet">
<style>
  :root {
    --page: #ffffff;
    --sun-yellow: #fcec00;
    --ink: #050505;
    --signal-red: #ee3234;
    --paper-white: #f4f4f4;
    --gear-shadow: #d9c900;
  }
  * { margin: 0; padding: 0; box-sizing: border-box; }
  html, body {
    width: 1200px;
    height: 1000px;
    overflow: hidden;
    background: var(--page);
  }
  .canvas {
    position: relative;
    width: 1200px;
    height: 1000px;
    background: var(--page);
  }
  .ad-banner {
    position: absolute;
    left: 2px;
    top: 187px;
    width: 1196px;
    height: 626px;
    background: var(--sun-yellow);
    overflow: hidden;
  }
  .headline {
    position: absolute;
    left: 46px;
    top: 196px;
    font-family: "Bebas Neue", "Oswald", sans-serif;
    font-size: 101px;
    line-height: 1;
    color: var(--ink);
    letter-spacing: 0.5px;
    white-space: nowrap;
  }
  .headline-bar {
    position: absolute;
    left: 0;
    top: 284px;
    width: 750px;
    height: 86px;
    background: var(--ink);
  }
  .event-tag {
    position: absolute;
    left: 648px;
    top: 238px;
    width: 548px;
    height: 102px;
    background: var(--signal-red);
    color: var(--paper-white);
    text-align: right;
    padding-right: 10px;
  }
  .event-name {
    font-family: "Bebas Neue", "Oswald", sans-serif;
    font-size: 67px;
    line-height: 1;
    margin-top: 12px;
    letter-spacing: 0.5px;
  }
  .event-type {
    font-family: "PT Sans Narrow", "Arial Narrow", sans-serif;
    font-size: 21px;
    line-height: 1;
    margin-top: -1px;
    letter-spacing: 0.4px;
  }
  .event-details {
    position: absolute;
    left: 46px;
    top: 381px;
    font-family: "PT Sans Narrow", "Arial Narrow", sans-serif;
    font-size: 18.5px;
    line-height: 22px;
    color: var(--ink);
    letter-spacing: 0.3px;
    text-transform: uppercase;
  }
  .gear-visual {
    position: absolute;
    left: 676px;
    top: 370px;
    width: 510px;
    height: 190px;
  }
</style>
</head>
<body>
  <div class="canvas">
    <section class="ad-banner">
      <h1 class="headline">Let’s Play Ball</h1>
      <div class="headline-bar"></div>

      <div class="event-tag">
        <h2 class="event-name">Spring Swing</h2>
        <p class="event-type">SOFTBALL AND KICKBALL TOURNAMENT</p>
      </div>

      <p class="event-details">
        Saturday April 12th / Lakeview &amp; Harbor Ave<br>
        Men’s &amp; Coed 12”&amp;16” / Coed Kickball
      </p>

      <svg class="gear-visual" viewBox="0 0 510 190" role="img" aria-label="Photo of a softball bat, ball and black batting helmet lying on the ground">
        <defs>
          <radialGradient id="gear-tone" cx="0.55" cy="0.55" r="0.6">
            <stop offset="0" stop-color="#3a3a3a"/>
            <stop offset="0.55" stop-color="#8c8a5a"/>
            <stop offset="1" stop-color="#fcec00"/>
          </radialGradient>
        </defs>
        <rect width="510" height="190" fill="url(#gear-tone)"/>
      </svg>
    </section>
  </div>
</body>
</html>
```